Business Card Design REAL ESTATE SALES PLEASE DESIGN MY CARD 2COLOR CARD WITH RED AS THE DOMINANT

MOOR PINE REALTY
TorVHA Lic# 04827316
WALTER " WALT " KOVIC Tel 510 555-0142
TorVHA Lic# 00762408 Fax 510 555-0187
Email: walt@waltkovic.example Cell 510 555-0163
48610 FERNHILL COURT UNION CITY, CA 94999

Business

WALTER " WALT " KOVIC
TEL: 510 555-0142 FAX 510 555-0187
Address: 48610 Fernhill Court Union City , CA
EMAIL ADDRESS: walt@waltkovic.example

```html
<!DOCTYPE html>
<html lang="en">
<head>
<meta charset="utf-8">
<title>Moor Pine Realty – Business Card</title>
<link href="https://fonts.googleapis.com/css2?family=Lato:wght@400;700;900&display=swap" rel="stylesheet">
<style>
  :root{
    --red:#d8112a;
    --red-light:#e84a5f;
    --dark:#2a2a2c;
    --dark-deep:#161617;
    --white:#ffffff;
    --grey-text:#3a3a3a;
    --stage:#e8e6e3;
  }
  *{box-sizing:border-box;margin:0;padding:0}
  html,body{width:1200px;height:913px;overflow:hidden;background:var(--stage);font-family:"Lato",sans-serif}
  .card{position:absolute;width:540px;height:309px;overflow:hidden;box-shadow:0 14px 30px rgba(0,0,0,.28)}
  .card--back{left:50px;top:110px;background:linear-gradient(160deg,#3a3a3c,var(--dark-deep))}
  .card--front{left:610px;top:490px;background:var(--white)}

  .brand{position:absolute;display:flex;align-items:center;gap:10px}
  .brand__mark{width:26px;height:26px;background:var(--red);border-radius:4px}
  .brand__name{color:var(--red);font-weight:400;font-size:19px;letter-spacing:2px;line-height:1}

  /* back face */
  .back__band{position:absolute;left:0;top:172px;width:310px;height:72px;background:var(--white)}
  .back__block{position:absolute;left:300px;top:96px;width:190px;height:96px;background:linear-gradient(180deg,var(--red-light),var(--red));box-shadow:-6px 6px 14px rgba(0,0,0,.35)}
  .card--back .brand{left:28px;top:195px}

  /* front face */
  .card--front .brand{left:300px;top:44px}
  .front__name{position:absolute;left:0;top:104px;width:270px;height:50px;background:linear-gradient(180deg,var(--red-light),var(--red));clip-path:polygon(0 0,100% 0,88% 100%,0 100%);color:var(--white);font-weight:900;font-size:17px;letter-spacing:.5px;display:flex;align-items:center;padding-left:22px}
  .front__stripe{position:absolute;left:0;top:154px;width:14px;height:26px;background:var(--red)}
  .front__info{position:absolute;left:0;top:180px;width:540px;height:84px;background:linear-gradient(180deg,#3b3b3d,var(--dark-deep));color:var(--white);font-size:11.5px;padding:12px 0 0 40px}
  .front__rule{position:absolute;left:250px;top:166px;width:290px;height:4px;background:var(--red)}
  .front__panel{position:absolute;left:400px;top:96px;width:150px;height:74px;background:var(--dark);border:5px solid var(--red);border-radius:12px}
  .info__address{margin-bottom:8px}
  .info__row{display:flex;gap:34px}
  .info__col{display:flex;flex-direction:column;gap:6px}
  .contact{display:flex;align-items:center;gap:8px}
  .contact__icon{width:16px;height:16px;background:var(--red);border-radius:3px;display:flex;align-items:center;justify-content:center}
  .contact__icon svg{width:10px;height:10px;fill:var(--white)}
</style>
</head>
<body>
  <section class="card card--back" aria-label="Card back">
    <div class="back__band"></div>
    <div class="back__block"></div>
    <div class="brand">
      <span class="brand__mark"></span>
      <span class="brand__name">MOOR PINE REALTY</span>
    </div>
  </section>

  <section class="card card--front" aria-label="Card front">
    <div class="brand">
      <span class="brand__mark"></span>
      <span class="brand__name">MOOR PINE REALTY</span>
    </div>
    <div class="front__panel"></div>
    <div class="front__name">WALTER " WALT " KOVIC</div>
    <div class="front__stripe"></div>
    <div class="front__info">
      <p class="info__address">48610 Fernhill Court Union City , CA</p>
      <div class="info__row">
        <div class="info__col">
          <span class="contact">
            <span class="contact__icon"><svg viewBox="0 0 10 10"><path d="M2 1h2l1 2-1 1a5 5 0 0 0 2 2l1-1 2 1v2a1 1 0 0 1-1 1A8 8 0 0 1 1 2a1 1 0 0 1 1-1z"/></svg></span>
            (510) 555-0142
          </span>
          <span class="contact">
            <span class="contact__icon"><svg viewBox="0 0 10 10"><rect x="3" y="1" width="4" height="3"/><rect x="1" y="4" width="8" height="4" rx="1"/><rect x="3" y="7" width="4" height="2"/></svg></span>
            (510) 555-0187
          </span>
        </div>
        <div class="info__col">
          <span class="contact">
            <span class="contact__icon"><svg viewBox="0 0 10 10"><path d="M1 2h8v6H1z M1 2l4 3 4-3" fill="none" stroke="#fff" stroke-width="1"/></svg></span>
            walt@waltkovic.example
          </span>
        </div>
      </div>
    </div>
    <div class="front__rule"></div>
  </section>
</body>
</html>
```